Valbrook Data Works

Our company is about IT hardwares and IT solutions. IT hardware such as PC, RAMS, storage and servers. IT solutions such as project management, BA. We are also selling new technology too.

Target Market(s)

Consumer, Small to Medium Business, Corporate

Requirements
Must have
• The business card must have the following:
• Name:
• Title:
• Contact Number:
• Email address:
• Website:
• Color: Must match the logo color upgrade

```html
<!DOCTYPE html>
<html lang="en">
<head>
<meta charset="UTF-8">
<title>Valbrook Data Works – Business Card</title>
<link href="https://fonts.googleapis.com/css2?family=Exo+2:wght@700;800&family=Montserrat:wght@400;500;700&display=swap" rel="stylesheet">
<style>
  :root {
    --backdrop: #2b2b2b;
    --card: #1f1f1f;
    --card-edge: #262626;
    --ink: #f2f2f2;
    --ink-soft: #d9d9d9;
    --copper: #d98a34;
    --divider: #6a6a6a;
  }
  * { box-sizing: border-box; margin: 0; padding: 0; }
  html, body {
    width: 1200px;
    height: 900px;
    overflow: hidden;
    background: var(--backdrop);
  }
  .canvas {
    position: relative;
    width: 1200px;
    height: 900px;
    display: flex;
    flex-direction: column;
    align-items: center;
    justify-content: center;
    gap: 40px;
  }
  .card {
    width: 720px;
    height: 400px;
    background: var(--card);
    border: 1px solid var(--card-edge);
    box-shadow: 0 14px 30px rgba(0,0,0,0.45);
    position: relative;
  }

  /* Front */
  .card--front {
    display: flex;
    flex-direction: column;
    align-items: center;
    justify-content: center;
  }
  .brand {
    display: flex;
    align-items: center;
    gap: 14px;
  }
  .brand__dot {
    width: 16px;
    height: 16px;
    background: var(--copper);
  }
  .brand__name {
    font-family: "Montserrat", sans-serif;
    font-weight: 700;
    color: var(--ink);
    letter-spacing: 1px;
    text-transform: uppercase;
    line-height: 1;
  }
  .card--front .brand__name { font-size: 38px; }
  .card--front .front__web {
    margin-top: 64px;
    font-family: "Montserrat", sans-serif;
    font-size: 15px;
    color: var(--ink-soft);
    letter-spacing: 0.5px;
  }

  /* Back */
  .card--back {
    display: flex;
    align-items: center;
  }
  .back__brand {
    width: 370px;
    display: flex;
    justify-content: center;
    padding-left: 20px;
  }
  .card--back .brand__name {
    font-size: 26px;
    line-height: 1.15;
  }
  .back__divider {
    width: 1px;
    height: 200px;
    background: var(--divider);
  }
  .contact {
    padding-left: 34px;
    font-family: "Montserrat", sans-serif;
    color: var(--ink);
  }
  .contact__name {
    font-family: "Exo 2", sans-serif;
    font-weight: 800;
    font-size: 25px;
    color: var(--copper);
    text-transform: uppercase;
    letter-spacing: 0.5px;
  }
  .contact__title {
    font-size: 17px;
    margin-top: 2px;
  }
  .contact__address {
    font-size: 17px;
    margin-top: 18px;
    line-height: 1.3;
  }
  .contact__list {
    list-style: none;
    margin-top: 16px;
  }
  .contact__item {
    display: flex;
    align-items: center;
    gap: 14px;
    font-size: 17px;
    line-height: 1.55;
  }
  .contact__icon {
    width: 18px;
    height: 18px;
    flex: none;
  }
</style>
</head>
<body>
  <main class="canvas">
    <section class="card card--front">
      <div class="brand">
        <span class="brand__dot"></span>
        <span class="brand__name">Valbrook Data Works</span>
      </div>
      <p class="front__web">www.valbrookdata.com</p>
    </section>

    <section class="card card--back">
      <div class="back__brand">
        <div class="brand">
          <span class="brand__dot"></span>
          <span class="brand__name">Valbrook<br>Data Works</span>
        </div>
      </div>
      <div class="back__divider"></div>
      <div class="contact">
        <h2 class="contact__name">Daniel Ferris</h2>
        <p class="contact__title">Managing Director</p>
        <p class="contact__address">Linden Street 48<br>2010 Northvale Park</p>
        <ul class="contact__list">
          <li class="contact__item">
            <svg class="contact__icon" viewBox="0 0 24 24" fill="none" stroke="#d98a34" stroke-width="1.8" stroke-linejoin="round"><path d="M5 3h4l2 5-2.5 1.5a11 11 0 0 0 6 6L16 13l5 2v4a2 2 0 0 1-2 2A16 16 0 0 1 3 5a2 2 0 0 1 2-2z"/></svg>
            <span>+ 12 555 0190 42</span>
          </li>
          <li class="contact__item">
            <svg class="contact__icon" viewBox="0 0 24 24" fill="none" stroke="#d98a34" stroke-width="1.8"><rect x="3" y="5" width="18" height="14"/><path d="M3 5l9 8 9-8"/></svg>
            <span>daniel@valbrookdata.com</span>
          </li>
          <li class="contact__item">
            <svg class="contact__icon" viewBox="0 0 24 24" fill="none" stroke="#d98a34" stroke-width="1.6"><circle cx="12" cy="12" r="9"/><ellipse cx="12" cy="12" rx="4" ry="9"/><path d="M3 12h18M5 7h14M5 17h14"/></svg>
            <span>www.valbrookdata.com</span>
          </li>
        </ul>
      </div>
    </section>
  </main>
</body>
</html>
```